Tutoring Company Needs a Convincing Brochure

We need a tri-fold brochure for our tutoring/academic enrichment program. TRIM Study House was established in 2000 and is a small business that has thrived in a very competitive and crowded educational market among high profile companies like Vorel and Dastry. We offer intimate, affordable academic services for students grades 1-8. At TRIM, our teachers teach! We focus on small group settings, getting to know the families we work with, and engaging teachers that excite students to learn. Our brochure needs to convince parents that we are professional, nurturing and the best choice for their child to reach academic success. We are open minded in the design.

Target Market(s)

parents

Industry/Entity Type

Tutoring

Colors

Designer to choose colors to be used in the design.

Requirements
Must have
• Tri-Fold design, concise, convincing
Nice to have
• Diversity in images

```html
<!DOCTYPE html>
<html lang="en">
<head>
<meta charset="utf-8">
<title>TRIM Study House – Tri-fold Brochure</title>
<link href="https://fonts.googleapis.com/css2?family=Open+Sans:wght@400;600;700;800&display=swap" rel="stylesheet">
<style>
:root{
  --green:#6cb33f;
  --orange:#f6a01a;
  --orange-text:#e8701d;
  --navy:#3d4466;
  --blue:#2aa6dd;
  --white:#ffffff;
  --ink:#4a4a4a;
  --muted:#8a8a8a;
  --stage:#e4e4e4;
}
*{box-sizing:border-box;margin:0;padding:0}
html,body{width:1200px;height:2400px;overflow:hidden}
body{background:var(--stage);font-family:"Open Sans",Arial,sans-serif;color:var(--ink);position:relative}
.spread{position:absolute;left:50px;width:1100px;height:850px;background:var(--white);box-shadow:0 10px 30px rgba(0,0,0,.18);overflow:hidden}
.spread--outside{top:250px}
.spread--inside{top:1300px}
.spread__shapes{position:absolute;inset:0;width:1100px;height:850px}
.fold{position:absolute;top:0;bottom:0;width:1px;background:rgba(0,0,0,.08)}
.block{position:absolute}
.band-title{color:var(--white);font-weight:800;font-size:22px;letter-spacing:.5px}
.sub{font-weight:800;font-size:13px;text-transform:uppercase;line-height:1.3}
.body-text{font-size:12px;line-height:1.5}
.price-row{display:flex;justify-content:space-between;font-size:11.5px;line-height:1.6;color:var(--white)}
.wordmark{font-weight:800;font-size:28px;color:var(--navy);line-height:1;white-space:nowrap}
.slogan{font-weight:600;font-size:15px;color:var(--muted);margin-top:8px}
.headline{font-weight:800;text-transform:uppercase;line-height:1.15}
.contact-row{display:flex;align-items:center;gap:14px;font-size:14px;color:var(--ink);height:30px}
.contact-row__tab{width:56px;height:24px;display:flex;align-items:center;justify-content:center}
.list{list-style:none;font-size:12px;line-height:1.55;color:var(--white)}
.feature{position:absolute;left:0;width:367px;display:flex;gap:16px;padding:18px 22px;color:var(--white)}
.feature__icon{flex:none;width:48px;height:48px}
.quote{font-size:11.5px;line-height:1.5;color:var(--ink);display:flex;gap:8px}
.quote__mark{font-size:34px;font-weight:800;color:var(--blue);line-height:.8}
</style>
</head>
<body>

<section class="spread spread--outside" aria-label="Brochure outside spread">
  <svg class="spread__shapes" viewBox="0 0 1100 850">
    <defs>
      <linearGradient id="photoWarm" x1="0" y1="0" x2="1" y2="1">
        <stop offset="0" stop-color="#efe3d8"/><stop offset=".5" stop-color="#d9a98f"/><stop offset="1" stop-color="#7fc4da"/>
      </linearGradient>
      <radialGradient id="photoRound" cx=".5" cy=".45" r=".6">
        <stop offset="0" stop-color="#e8c2a8"/><stop offset=".7" stop-color="#6d5a52"/><stop offset="1" stop-color="#2f2a35"/>
      </radialGradient>
    </defs>
    <rect x="0" y="0" width="367" height="850" fill="var(--green)"/>
    <polygon points="0,40 300,40 280,90 0,90" fill="var(--navy)"/>
    <polygon points="367,0 733,0 733,170 367,290" fill="var(--orange)"/>
    <polygon points="367,290 733,170 733,620 367,690" fill="var(--navy)"/>
    <circle cx="550" cy="360" r="80" fill="url(#photoRound)" stroke="var(--white)" stroke-width="7" role="img" aria-label="Photo: smiling young student at a desk"/>
    <polygon points="733,170 1100,170 1100,470 733,600" fill="url(#photoWarm)" role="img" aria-label="Photo: teacher and girl student smiling together at a table"/>
    <polygon points="733,600 950,523 733,700" fill="var(--navy)"/>
    <polygon points="950,523 1100,470 1100,560 733,720 733,700" fill="var(--green)"/>
  </svg>
  <div class="fold" style="left:367px"></div>
  <div class="fold" style="left:733px"></div>

  <div class="block" style="left:24px;top:48px"><span class="band-title">PRICING</span></div>
  <div class="block" style="left:24px;top:112px;width:320px;color:var(--white)">
    <p class="sub">Small Group<br>Tutoring &amp; Enrichment</p>
    <div style="margin-top:6px">
      <div class="price-row"><span>One subject, weekly</span><span>$180 per month</span></div>
      <div class="price-row"><span>Two subjects, weekly</span><span>$275 per month</span></div>
      <div class="price-row"><span>Three subjects, weekly</span><span>$370 per month</span></div>
      <div class="price-row"><span>Four subjects, weekly</span><span>$450 per month</span></div>
    </div>
    <p class="sub" style="margin-top:16px">Add more, learn more</p>
    <div style="margin-top:4px">
      <div class="price-row"><span>Extra weekly session</span><span>$80 per month</span></div>
      <div class="price-row"><span>Homework help hour</span><span>$55 per month</span></div>
      <div class="price-row"><span>Reading club pass</span><span>$40 per month</span></div>
    </div>
    <p class="sub" style="margin-top:16px">1-on-1 Tutoring with a<br>credentialed classroom teacher</p>
    <div style="margin-top:4px">
      <div class="price-row"><span>Single hour</span><span>$65 per hour</span></div>
      <div class="price-row"><span>Package of five</span><span>$60 per hour</span></div>
      <div class="price-row"><span>Package of ten</span><span>$55 per hour</span></div>
    </div>
    <p class="sub" style="margin-top:16px">Save 10% by referring a new student</p>
    <p class="body-text" style="margin-top:4px">Siblings and returning families save on every month they enroll together.</p>
    <div style="margin-top:10px">
      <div class="price-row"><span>10% discount</span><span>second child</span></div>
      <div class="price-row"><span>15% discount</span><span>third child</span></div>
      <div class="price-row"><span>20% discount</span><span>full year paid</span></div>
    </div>
  </div>

  <div class="block headline" style="left:395px;top:40px;width:310px;color:var(--white);font-size:21px;text-align:center">Come in today to meet our teachers. We are ready to excite your child to learn.</div>
  <div class="block" style="left:385px;top:455px;width:330px;text-align:center">
    <p class="wordmark" style="font-size:21px;color:var(--white)">TRIM Study House</p>
    <p style="font-weight:600;font-size:12px;color:var(--orange);margin-top:6px">Small groups. Big progress.</p>
    <p style="color:var(--white);font-size:12.5px;line-height:1.55;margin-top:12px">Bayview / 214 Alder St.<br>Monday – Friday 2–8pm<br>Westfield / 58 Orchard Plaza<br>Monday, Wednesday 3–8, Saturday 10–1</p>
  </div>
  <div class="block" style="left:380px;top:715px;width:340px">
    <div class="contact-row">
      <span class="contact-row__tab" style="background:var(--orange)"><svg width="14" height="14" viewBox="0 0 24 24"><path d="M6 2h4l2 5-3 2a12 12 0 0 0 6 6l2-3 5 2v4a2 2 0 0 1-2 2A18 18 0 0 1 4 4a2 2 0 0 1 2-2z" fill="#fff"/></svg></span>
      <span>(555) 010-4827</span></div>
    <div class="contact-row">
      <span class="contact-row__tab" style="background:var(--navy)"><svg width="16" height="12" viewBox="0 0 24 18"><rect x="1" y="1" width="22" height="16" fill="none" stroke="#fff" stroke-width="2"/><path d="M1 1l11 9 11-9" fill="none" stroke="#fff" stroke-width="2"/></svg></span>
      <span>hello@trimstudy.org</span></div>
    <div class="contact-row">
      <span class="contact-row__tab" style="background:var(--blue)"><svg width="14" height="14" viewBox="0 0 24 24"><circle cx="12" cy="12" r="10" fill="none" stroke="#fff" stroke-width="2"/><path d="M2 12h20M12 2c4 4 4 16 0 20M12 2c-4 4-4 16 0 20" fill="none" stroke="#fff" stroke-width="2"/></svg></span>
      <span>www.trimstudy.org</span></div>
  </div>

  <div class="block" style="left:765px;top:60px;width:310px">
    <p class="wordmark">TRIM Study House</p>
    <p class="slogan">Small groups. Big progress.</p>
  </div>
  <div class="block" style="right:22px;top:730px;width:350px;text-align:right">
    <p class="headline" style="color:var(--orange-text);font-size:21px">Our inspiring, engaging<br>teachers teach<br>to the common core.</p>
    <p style="font-size:11px;color:var(--muted);margin-top:6px">TRIM Study House, a non-profit tutoring organization</p>
  </div>
</section>

<section class="spread spread--inside" aria-label="Brochure inside spread">
  <svg class="spread__shapes" viewBox="0 0 1100 850">
    <defs>
      <linearGradient id="photoClass" x1="0" y1="0" x2="1" y2="1">
        <stop offset="0" stop-color="#c98f6a"/><stop offset=".45" stop-color="#e8d6c4"/><stop offset=".75" stop-color="#f0b04a"/><stop offset="1" stop-color="#6b8fb8"/>
      </linearGradient>
    </defs>
    <rect x="0" y="0" width="367" height="470" fill="var(--green)"/>
    <polygon points="0,40 260,40 240,85 0,85" fill="var(--navy)"/>
    <rect x="0" y="470" width="367" height="125" fill="var(--orange)"/>
    <rect x="0" y="595" width="367" height="125" fill="var(--navy)"/>
    <rect x="0" y="720" width="367" height="130" fill="var(--blue)"/>
    <polygon points="367,0 1100,0 1100,250 367,420" fill="url(#photoClass)" role="img" aria-label="Photo: teacher working with a small group of diverse children at a table"/>
    <polygon points="367,420 1100,250 1100,580 367,690" fill="var(--navy)"/>
    <polygon points="367,700 600,700 580,736 367,736" fill="var(--orange)"/>
  </svg>
  <div class="fold" style="left:367px"></div>
  <div class="fold" style="left:733px"></div>

  <div class="block" style="left:24px;top:48px"><span class="band-title">WHO ARE WE</span></div>
  <div class="block body-text" style="left:24px;top:105px;width:320px;color:var(--white)">
    <p>At TRIM, we teach. TRIM's Ready diagnostic and Ready curriculum guide our teachers to target exactly what your child needs to learn.</p>
    <p style="margin-top:10px">Our teachers engage, instruct and excite every child to understand, enjoy and succeed in academics.</p>
    <p style="margin-top:10px">Each student's lesson plan is personalized to meet their academic level. We strengthen foundational skills and ensure students are challenged.</p>
    <p style="margin-top:10px">TRIM develops independent learners by instilling positive attitudes toward learning, building academic confidence and teaching skills needed for your child to thrive in school.</p>
  </div>
  <div class="feature" style="top:470px;height:125px">
    <svg class="feature__icon" viewBox="0 0 48 48"><rect x="8" y="6" width="28" height="36" fill="none" stroke="#fff" stroke-width="2.5"/><path d="M13 16l3 3 5-6M13 28l3 3 5-6" fill="none" stroke="#fff" stroke-width="2.5"/><path d="M25 17h7M25 29h7" stroke="#fff" stroke-width="2.5"/></svg>
    <div><p class="sub">We test for success 3 times per year</p><p class="body-text" style="font-size:11px;margin-top:4px">Our progress assessments measure growth so parents see exactly how far their child has come.</p></div>
  </div>
  <div class="feature" style="top:595px;height:125px">
    <svg class="feature__icon" viewBox="0 0 48 48"><path d="M2 18l22-10 22 10-22 10z" fill="#fff"/><path d="M12 23v10c6 5 18 5 24 0V23" fill="none" stroke="#fff" stroke-width="2.5"/><path d="M42 20v12" stroke="#fff" stroke-width="2.5"/></svg>
    <div><p class="sub">TRIM builds confident students</p><p class="body-text" style="font-size:11px;margin-top:4px">Our teachers help develop independent, confident learners who are ready for every new grade level.</p></div>
  </div>
  <div class="feature" style="top:720px;height:130px">
    <svg class="feature__icon" viewBox="0 0 48 48"><circle cx="16" cy="16" r="7" fill="none" stroke="#fff" stroke-width="2.5"/><circle cx="33" cy="18" r="6" fill="none" stroke="#fff" stroke-width="2.5"/><path d="M3 40c0-9 6-13 13-13s13 4 13 13M26 40c1-7 4-10 8-10 6 0 10 4 10 10" fill="none" stroke="#fff" stroke-width="2.5"/></svg>
    <div><p class="sub">1-on-1 Tutoring</p><p class="body-text" style="font-size:11px;margin-top:4px">Private sessions with a credentialed teacher, tailored to your child's goals and schedule.</p></div>
  </div>

  <div class="block" style="left:392px;top:432px;width:320px;color:var(--white)">
    <p class="headline" style="font-size:24px">At TRIM,<br>teachers teach.</p>
    <p class="body-text" style="font-size:11px;margin-top:6px">Established in 2000, TRIM Study House's mission is to create a nurturing environment that fosters a love of learning. Our engaged teachers know every family we serve.</p>
    <p class="sub" style="color:var(--orange);margin-top:10px">Choose what to study</p>
    <ul class="list" style="font-size:11px;line-height:1.45">
      <li>TRIM's Ready Math</li><li>TRIM's Ready Reading</li><li>TRIM's Ready Writing/Grammar</li><li>School Homework Help</li><li>Includes all subjects</li>
    </ul>
  </div>
  <div class="block" style="left:385px;top:707px"><span style="color:var(--white);font-weight:800;font-size:16px">TESTIMONIALS</span></div>
  <div class="block quote" style="left:385px;top:752px;width:330px">
    <span class="quote__mark">“</span>
    <p>The teachers are patient, friendly and most importantly engaging when it comes to helping my sister with her schoolwork. She loves it. – Marla T.</p>
  </div>

  <div class="block" style="left:760px;top:345px;width:310px;color:var(--white)">
    <p class="sub" style="color:var(--orange)">Tutoring &amp; Enrichment</p>
    <ul class="list"><li>Small Group Tutoring (1–8)</li><li>Study Skills (Grades 4–8)</li><li>High School Prep (7–8)</li><li>SAT/ACT Prep</li><li>1-on-1 Tutoring (K–12)</li></ul>
    <p class="sub" style="color:var(--orange);margin-top:10px">After School</p>
    <ul class="list"><li>Homework support, Monday to Friday</li><li>Everyday enrichment in all subjects</li></ul>
    <p class="sub" style="color:var(--orange);margin-top:10px">Technology Programs</p>
    <ul class="list"><li>Coding &amp; Typing</li><li>Kids Code</li></ul>
  </div>
  <div class="block quote" style="left:760px;top:680px;width:320px">
    <span class="quote__mark">“</span>
    <p>My children have come here for 2 years now. They liked it. When we drive by they still talk about how they liked it there. – Owen K.</p>
  </div>
</section>

</body>
</html>
```